Consulting Firm stationery design

Now that the MakerHive has given us a new logo we'll now need to have all our stationery designed. So we're asking for this community to help us once again.We're looking to get from you Letterheads (Header and Footer, suitable to be applied on a .docx format. Vectors are required but keep this in mind), Envelopes (Front and Back designs, back is not a must but desirable depending on your design), 9"x 12" Pocket Folders (consider design for front and back, also for pockets as well), Business Cards.An elegant design is a must have, mostly for Folders and Envelopes. The idea with this two is to stand out from others when they're handed over. Ideas are welcomed, we were thinking maybe on some texturing simulation for these.Folders will have 3 addresses and contact information. Envelopes will have 1 address and contact information.Brand Manual attached. vendaluxo logo has been copyrighted already. I'm also attaching the current stationary designs (these never got to be out for production but was going to be before we made the brand changes); Pocker folders page 1 to 4 (pages 2 and 4 are the pocket designs), Pages 5 and 6 (6 is the back of the envelope), Pages 7 and 8 (8 is the back of the business card). No letterhead within these designs as it just had the logo and address.

Industry/Entity Type

Business Consultant

Font styles to use
Serif
Sans Serif

Requirements
Must have
• Elegance
Nice to have
• Modern looking out of common

```html
<!DOCTYPE html>
<html lang="en">
<head>
<meta charset="utf-8">
<title>vendaluxo business card</title>
<link href="https://fonts.googleapis.com/css2?family=Poppins:wght@300;400;500;600&display=swap" rel="stylesheet">
<style>
  :root {
    --stage: #2e2e2e;
    --card: #ffffff;
    --ink: #3d3d3d;
    --ink-soft: #4a4a4a;
    --brand-blue: #1a6fa3;
    --band: #383838;
    --band-text: #ffffff;
    --pattern-a: #f4f6fa;
    --pattern-b: #ffffff;
  }
  * { box-sizing: border-box; margin: 0; padding: 0; }
  html, body {
    width: 1200px; height: 960px; overflow: hidden;
    background: var(--stage);
    font-family: "Poppins", sans-serif;
    color: var(--ink);
  }
  .card {
    position: absolute; left: 261px; width: 679px; height: 387px;
    background: var(--card);
    box-shadow: 0 4px 14px rgba(0,0,0,.45);
    overflow: hidden;
  }
  .card--front { top: 61px; }
  .card--back { top: 511px; }

  .contact { position: absolute; left: 45px; top: 36px; font-size: 14.5px; line-height: 17.4px; color: var(--ink-soft); font-weight: 300; }
  .contact__name { font-size: 18.5px; font-weight: 600; color: var(--ink); line-height: 24px; }
  .contact__role { font-size: 16px; font-weight: 300; }
  .contact__creds { font-size: 12.5px; line-height: 14.5px; margin-bottom: 7px; }
  .contact__group { margin-bottom: 9px; }
  .contact__company { font-weight: 500; color: var(--ink); }
  .contact__link { color: var(--brand-blue); }
  .contact__services { color: var(--brand-blue); font-weight: 400; font-size: 14.5px; }

  .front-mark { position: absolute; right: 46px; top: 298px; display: flex; align-items: center; gap: 8px; }
  .front-mark__dot { width: 16px; height: 16px; border-radius: 50%; background: var(--brand-blue); }
  .front-mark__name { font-size: 22px; font-weight: 600; color: var(--brand-blue); }

  .back-pattern { position: absolute; inset: 0; background: linear-gradient(180deg, var(--pattern-a), var(--pattern-b) 50%, var(--pattern-a)); }

  .back-mark { position: absolute; left: 0; right: 0; top: 106px; display: flex; justify-content: center; align-items: center; gap: 12px; }
  .back-mark__name { font-size: 70px; font-weight: 500; color: var(--ink); letter-spacing: -1px; line-height: 1; }
  .back-mark__dot { width: 26px; height: 26px; border-radius: 50%; background: var(--brand-blue); }

  .partner-band {
    position: absolute; left: 0; right: 0; top: 320px; height: 35px;
    background: var(--band);
    display: flex; align-items: center; justify-content: space-between;
    padding: 0 48px 0 37px;
  }
  .partner-band__name { color: var(--band-text); font-size: 20px; font-weight: 500; }
  .partner-band__name--small { font-size: 13px; font-weight: 600; }
</style>
</head>
<body>
  <section class="card card--front">
    <div class="contact">
      <p class="contact__name">Marcel T. Duran <span class="contact__role">| COO &amp; Partner</span></p>
      <p class="contact__creds">BSc, MScIS, Nodara Certified, CRDA<br>Risk&amp;DataAnalytics</p>
      <div class="contact__group">
        <p>(809) 555 0142 ext. 201</p>
        <p>(809) 555 0178</p>
        <p>marcel@vendaluxo.do</p>
      </div>
      <div class="contact__group">
        <p class="contact__company">VENDALUXO SRL</p>
        <p>Ceiba Business Plaza</p>
        <p>Av. Los Almendros 42, Naco</p>
        <p>Santiago, Rep. Dominicana</p>
      </div>
      <div class="contact__group">
        <p>(809) 555 0142</p>
        <p>info@vendaluxo.do</p>
        <p class="contact__link">www.vendaluxo.do</p>
      </div>
      <p>VENDALUXO SRL</p>
      <p>DR member firm of vendaluxo LLC</p>
      <p class="contact__services">Consultancy • Audit • Analytics</p>
    </div>
    <div class="front-mark">
      <span class="front-mark__dot"></span>
      <span class="front-mark__name">vendaluxo</span>
    </div>
  </section>

  <section class="card card--back">
    <div class="back-pattern" role="img" aria-label="Faint repeating pattern of soft grey rounded bars"></div>
    <div class="back-mark">
      <span class="back-mark__name">vendaluxo</span>
      <span class="back-mark__dot"></span>
    </div>
    <div class="partner-band">
      <span class="partner-band__name">Nodara</span>
      <span class="partner-band__name">Corvalis</span>
      <span class="partner-band__name partner-band__name--small">Pelvant</span>
    </div>
  </section>
</body>
</html>
```